Brightfold Sky Advisors needs a wordpress design

New consulting company based in San Francisco focusing on leading businesses (primarily startups) into the cloud. Services include: cloud architecture, security, automation, back-end design, Infrastructure Optimization, Capacity Planning. Even though we are a new company, I'd like to convey a sense of confidence to the prospective client. Logos are attached

Target Market(s)

Start-ups looking to move their application into the cloud

Industry/Entity Type

Information Technology

```html
<!DOCTYPE html>
<html lang="en">
<head>
<meta charset="utf-8">
<title>Brightfold Sky Advisors</title>
<link href="https://fonts.googleapis.com/css2?family=Open+Sans:wght@400;600;700;800&display=swap" rel="stylesheet">
<style>
:root{
  --blue:#1e8bc3;
  --blue-dark:#176d9a;
  --ink:#2f3337;
  --muted:#6b7074;
  --dark:#3e4349;
  --card-dark:#4a4f56;
  --footer:#2b2f33;
  --light:#eceeef;
  --white:#ffffff;
  --teal:#1aa7c2;
  --green:#8db51f;
  --navy:#1f4e79;
  --red:#e5532c;
}
*{box-sizing:border-box;margin:0;padding:0}
html,body{width:1200px;height:3000px;overflow:hidden}
body{font-family:"Open Sans",Arial,sans-serif;color:var(--ink);background:var(--white)}
.page{width:1200px;height:3000px;position:relative}

/* header */
.site-header{height:120px;position:relative;background:var(--white)}
.brand{position:absolute;left:60px;top:30px;display:flex;align-items:center;gap:12px}
.brand-mark{width:44px;height:44px;border-radius:50%;background:var(--blue)}
.brand-name{font-size:24px;font-weight:700;color:var(--blue);line-height:1.1;width:190px}
.contact-us{position:absolute;right:60px;top:14px;display:flex;align-items:center;gap:10px}
.contact-us small{display:block;font-size:11px;color:var(--muted);letter-spacing:1px}
.contact-us strong{font-size:20px;color:var(--blue);font-weight:700}
.main-nav{position:absolute;right:60px;top:88px;display:flex;gap:46px}
.main-nav a{font-size:14px;font-weight:600;color:var(--ink);text-decoration:none;letter-spacing:1px;padding-bottom:8px}
.main-nav a.active{border-bottom:3px solid var(--blue);color:var(--blue)}

/* hero */
.hero{height:540px;position:relative;background:linear-gradient(100deg,#5d6770 0%,#9aa3aa 45%,#d8dcdf 75%,#bfc5ca 100%)}
.hero-copy{position:absolute;left:64px;top:120px;color:var(--white)}
.hero-title{font-size:100px;font-weight:800;letter-spacing:3px;line-height:1}
.hero-sub{font-size:28px;font-weight:400;letter-spacing:3px;margin-top:14px;border-bottom:2px solid rgba(255,255,255,.7);display:inline-block;padding-bottom:6px}
.btn-outline{display:inline-block;border:2px solid var(--white);color:var(--white);font-size:20px;letter-spacing:2px;padding:12px 30px;margin-top:34px}

/* sections */
.section-title{font-size:40px;font-weight:800;text-align:center;letter-spacing:2px;color:var(--ink)}
.section-intro{width:760px;margin:18px auto 0;text-align:center;font-size:15px;line-height:1.6;color:var(--muted)}

.company{height:540px;padding-top:50px}
.services{width:1080px;margin:50px auto 0;display:grid;grid-template-columns:1fr 1fr;row-gap:50px;column-gap:60px}
.service{display:flex;gap:24px}
.service-icon{width:100px;height:100px;flex:none;display:flex;align-items:center;justify-content:center}
.service-icon.consulting{background:var(--teal)}
.service-icon.technology{background:var(--green)}
.service-icon.innovation{background:var(--navy)}
.service-icon.management{background:var(--red)}
.service h3{font-size:20px;font-weight:700;color:var(--blue);letter-spacing:1px;margin-top:2px}
.service p{font-size:14px;line-height:1.6;color:var(--muted);margin-top:8px}

.testimonial{height:460px;position:relative;background:linear-gradient(90deg,#2c3137 0%,#474e55 50%,#32383e 100%);color:var(--white);text-align:center}
.quote-mark{font-size:150px;font-weight:800;line-height:1;padding-top:60px;height:180px}
.quote-text{width:900px;margin:0 auto;font-size:22px;font-weight:700;line-height:1.5}
.quote-author{font-size:15px;margin-top:20px;color:#d0d4d8}
.testimonial .btn-outline{margin-top:26px}

.team{height:700px;padding-top:60px;background:var(--white)}
.team-cards{width:1060px;margin:50px auto 0;display:grid;grid-template-columns:repeat(3,1fr);gap:40px}
.member{height:460px;text-align:center;padding-top:36px}
.member.light{background:var(--white);box-shadow:0 4px 18px rgba(0,0,0,.22)}
.member.dark{background:var(--card-dark);color:var(--white)}
.avatar{width:160px;height:160px;border-radius:50%;margin:0 auto;border:6px solid #e8ebee;background:radial-gradient(circle at 50% 40%,#c9b29c 0%,#8d7e72 55%,#cfd5da 100%)}
.member h4{font-size:18px;font-weight:600;margin-top:26px;letter-spacing:1px}
.socials{display:flex;justify-content:center;gap:10px;margin-top:14px}
.socials span{width:30px;height:30px;border-radius:50%;background:var(--blue)}
.member p{font-size:14px;line-height:1.6;padding:20px 40px 0;color:inherit;opacity:.85}

.needs{height:460px;padding-top:50px;background:linear-gradient(180deg,#e4e7e9 0%,#f1f2f3 50%,#dfe2e4 100%)}
.needs .section-title{font-size:34px;letter-spacing:1px}
.needs-grid{width:1080px;margin:50px auto 0;display:grid;grid-template-columns:1fr 1fr;row-gap:50px;column-gap:60px}
.need{display:flex;gap:26px}
.need-icon{width:86px;height:86px;flex:none;border:3px solid var(--ink);border-radius:50%;display:flex;align-items:center;justify-content:center}
.need h3{font-size:18px;font-weight:700;letter-spacing:.5px}
.need p{font-size:14px;line-height:1.6;color:var(--muted);margin-top:8px}

.site-footer{height:160px;background:var(--footer);position:relative;color:#c9cdd1}
.footer-links{position:absolute;left:120px;top:36px;display:flex;gap:150px}
.footer-links ul{list-style:none}
.footer-links li{font-size:14px;font-weight:600;line-height:1.9;letter-spacing:.5px}
.footer-brand{position:absolute;right:70px;top:50px;display:flex;align-items:center;gap:12px}
.footer-brand .brand-mark{background:#8a9096}
.footer-brand .brand-name{color:#8a9096}
.copyright{height:20px;background:var(--blue);color:var(--white);font-size:11px;text-align:center;line-height:20px}
</style>
</head>
<body>
<div class="page">

<header class="site-header">
  <div class="brand"><span class="brand-mark"></span><span class="brand-name">Brightfold Sky Advisors</span></div>
  <div class="contact-us">
    <svg width="30" height="30" viewBox="0 0 24 24"><circle cx="12" cy="12" r="11" fill="none" stroke="#2f3337" stroke-width="1.5"/><path d="M8 6.5l2 .3.9 2.6-1.3 1.1a7 7 0 003.9 3.9l1.1-1.3 2.6.9.3 2c-.4.8-1.4 1.3-2.4 1.1A10 10 0 016.9 8.9c-.2-1 .3-2 1.1-2.4z" fill="#2f3337"/></svg>
    <div><small>CONTACT US TODAY</small><strong>1-888-555-0142</strong></div>
  </div>
  <nav class="main-nav">
    <a class="active" href="#">HOME</a><a href="#">ABOUT</a><a href="#">SERVICES</a><a href="#">PROJECTS</a><a href="#">CONTACTS</a>
  </nav>
</header>

<section class="hero" role="img" aria-label="Photo of a thoughtful businessman with glasses at a bright office desk">
  <div class="hero-copy">
    <div class="hero-title">SUCCEED!</div>
    <div class="hero-sub">CHANGE YOUR FUTURE!</div><br>
    <span class="btn-outline">LEARN MORE</span>
  </div>
</section>

<section class="company">
  <h2 class="section-title">THE COMPANY</h2>
  <p class="section-intro">Lorem ipsum dolor sit amet, consectetuer adipiscing elit. Praesent vestibulum molestie lacus. Aenean nonummy hendrerit mauris. Phasellus porta.</p>
  <div class="services">
    <div class="service">
      <div class="service-icon consulting"><svg width="54" height="54" viewBox="0 0 24 24" fill="#fff"><circle cx="12" cy="7" r="3"/><circle cx="5" cy="9" r="2.2"/><circle cx="19" cy="9" r="2.2"/><path d="M6 19c0-4 2.7-6 6-6s6 2 6 6z"/><path d="M1 18c0-3 1.8-4.5 4-4.5 1 0 1.6.3 2 .6-1 1-1.6 2.3-1.7 3.9z"/><path d="M23 18c0-3-1.8-4.5-4-4.5-1 0-1.6.3-2 .6 1 1 1.6 2.3 1.7 3.9z"/></svg></div>
      <div><h3>CONSULTING</h3><p>Lorem ipsum dolor sit amet, consectetuer adipiscing elit. Praesent vestibulum molestie lacus. Aenean nonummy hendrerit mauris. Phasellus porta.</p></div>
    </div>
    <div class="service">
      <div class="service-icon technology"><svg width="54" height="54" viewBox="0 0 24 24" fill="none" stroke="#fff" stroke-width="2.4"><circle cx="12" cy="12" r="3.5"/><path d="M12 2v4M12 18v4M2 12h4M18 12h4M4.9 4.9l2.8 2.8M16.3 16.3l2.8 2.8M4.9 19.1l2.8-2.8M16.3 7.7l2.8-2.8"/></svg></div>
      <div><h3>TECHNOLOGY</h3><p>Lorem ipsum dolor sit amet, consectetuer adipiscing elit. Praesent vestibulum molestie lacus. Aenean nonummy hendrerit mauris. Phasellus porta.</p></div>
    </div>
    <div class="service">
      <div class="service-icon innovation"><svg width="54" height="54" viewBox="0 0 24 24" fill="none" stroke="#fff" stroke-width="2"><rect x="4" y="5" width="16" height="11" rx="1"/><path d="M2 19h20"/></svg></div>
      <div><h3>INNOVATION</h3><p>Lorem ipsum dolor sit amet, consectetuer adipiscing elit. Praesent vestibulum molestie lacus. Aenean nonummy hendrerit mauris. Phasellus porta.</p></div>
    </div>
    <div class="service">
      <div class="service-icon management"><svg width="54" height="54" viewBox="0 0 24 24" fill="#fff"><path d="M3 9h4l8-5v16l-8-5H3z"/><path d="M18 8c1.5 1 1.5 7 0 8" stroke="#fff" stroke-width="2" fill="none"/></svg></div>
      <div><h3>MANAGEMENT</h3><p>Lorem ipsum dolor sit amet, consectetuer adipiscing elit. Praesent vestibulum molestie lacus. Aenean nonummy hendrerit mauris. Phasellus porta.</p></div>
    </div>
  </div>
</section>

<section class="testimonial" role="img" aria-label="Dim background photo of a businessman at work">
  <div class="quote-mark">&ldquo;</div>
  <p class="quote-text">Lorem ipsum dolor sit amet, consectetuer adipiscing elit. Praesent vestibulum molestie lacus. Aenean nonummy hendrerit mauris. Phasellus porta.</p>
  <p class="quote-author">Owen Carter, our best specialist</p>
  <span class="btn-outline">READ TESTIMONIALS</span>
</section>

<section class="team">
  <h2 class="section-title">MEET THE TEAM</h2>
  <p class="section-intro">Lorem ipsum dolor sit amet, consectetuer adipiscing elit. Praesent vestibulum molestie lacus. Aenean nonummy hendrerit mauris. Phasellus porta.</p>
  <div class="team-cards">
    <div class="member light">
      <div class="avatar" role="img" aria-label="Portrait photo of team member Daniel Reyes"></div>
      <h4>DANIEL REYES</h4>
      <div class="socials"><span></span><span></span><span></span></div>
      <p>Vivamus eget tellus in enim sollicitudin porta. Nunc egestas metus vel augue semper, nec facilisis purus cursus. Nulla posuere nisl sed mi.</p>
    </div>
    <div class="member dark">
      <div class="avatar" role="img" aria-label="Portrait photo of team member Helena Brooks"></div>
      <h4>HELENA BROOKS</h4>
      <div class="socials"><span></span><span></span><span></span></div>
      <p>Vivamus eget tellus in enim sollicitudin porta. Nunc egestas metus vel augue semper, nec facilisis purus cursus. Nulla posuere nisl sed mi.</p>
    </div>
    <div class="member dark">
      <div class="avatar" role="img" aria-label="Portrait photo of team member Marcus Lane"></div>
      <h4>MARCUS LANE</h4>
      <div class="socials"><span></span><span></span><span></span></div>
      <p>Vivamus eget tellus in enim sollicitudin porta. Nunc egestas metus vel augue semper, nec facilisis purus cursus. Nulla posuere nisl sed mi.</p>
    </div>
  </div>
</section>

<section class="needs" role="img" aria-label="Faint background photo of an office meeting">
  <h2 class="section-title">HELPING WITH ANY OF YOUR BUSINESS NEEDS</h2>
  <div class="needs-grid">
    <div class="need">
      <div class="need-icon"><svg width="42" height="42" viewBox="0 0 24 24" fill="none" stroke="#2f3337" stroke-width="1.8"><circle cx="12" cy="12" r="9"/><circle cx="12" cy="12" r="5"/><circle cx="12" cy="12" r="1.5" fill="#2f3337"/></svg></div>
      <div><h3>LOREM IPSUM IS SIMPLY DUMMY TEXT</h3><p>Provide technical and functional expertise to solve automation specific application problems by utilising best known industry practices.</p></div>
    </div>
    <div class="need">
      <div class="need-icon"><svg width="42" height="42" viewBox="0 0 24 24" fill="none" stroke="#2f3337" stroke-width="1.8"><path d="M4 4l16 16M20 4L4 20"/><path d="M3 3h4M17 3h4M3 21h4M17 21h4"/></svg></div>
      <div><h3>LOREM IPSUM IS SIMPLY DUMMY TEXT</h3><p>Provide senior experienced engineers to deliver long term improvements and cost reduction. Perform sizing calculations for new systems and plan capacity.</p></div>
    </div>
    <div class="need">
      <div class="need-icon"><svg width="42" height="42" viewBox="0 0 24 24" fill="none" stroke="#2f3337" stroke-width="1.8"><path d="M12 3a6 6 0 00-3.5 10.9V17h7v-3.1A6 6 0 0012 3z"/><path d="M9.5 20h5"/></svg></div>
      <div><h3>LOREM IPSUM IS SIMPLY DUMMY TEXT</h3><p>Develop systems and operational specifications for clients in the cloud and ensure efficient deployment. Collaborate with teams to migrate workloads.</p></div>
    </div>
    <div class="need">
      <div class="need-icon"><svg width="42" height="42" viewBox="0 0 24 24" fill="none" stroke="#2f3337" stroke-width="1.8"><circle cx="12" cy="12" r="3"/><path d="M12 2v3M12 19v3M2 12h3M19 12h3M5 5l2 2M17 17l2 2M5 19l2-2M17 7l2-2"/></svg></div>
      <div><h3>LOREM IPSUM IS SIMPLY DUMMY TEXT</h3><p>Provide objective technological designs for start-up teams. Drive improvements and cost reduction. Perform sizing calculations for systems in place today.</p></div>
    </div>
  </div>
</section>

<footer class="site-footer">
  <div class="footer-links">
    <ul><li>HOME</li><li>ABOUT US</li><li>PRODUCTS</li><li>CAREER</li></ul>
    <ul><li>CONTACT US</li><li>TERMS AND CONDITIONS</li><li>PRIVACY POLICY</li></ul>
  </div>
  <div class="footer-brand"><span class="brand-mark"></span><span class="brand-name">Brightfold Sky Advisors</span></div>
</footer>
<div class="copyright">Copyright 2015 Brightfold Sky Advisors. All rights reserved</div>

</div>
</body>
</html>
```